Wren Vehicle Polishing (Mobile detail)

I need a business card made up. I'd like it to be different in some form, either raised, embossed, debossed, something cool that stands out. (preferably embossed text somewhere in it). I will be including the Initial png file. Let me know if you need the photoshop of adobe illustrator file to work with.

Information to be included: Text: XXX-XXX-XXXX Phone: XXX-XXX-XXXX Email: wrenpolishcrew@mailbox-demo.net Website: www.socialpage-demo.net/wrenpolishKTR Hours of operation: Mon - Fri 7:00AM to 8:00PM Sat - 10:00AM to 8:00PM

Target Market(s)

Mobile automotive detailing

Industry/Entity Type

Automotive

Contact Information for Business Card

Make it stand out with embossed lettering, I'd also like the background to be glossy black or matte, something that represents a shiny car, black preferred

Requirements
Must have
• A glossy background, or something.
• My logo, pick one of them that best fits your design.
Should not have
• White background,
• something that does not stand out.

```html
<!DOCTYPE html>
<html lang="en">
<head>
<meta charset="utf-8">
<title>Wren Vehicle Polishing – Business Card</title>
<link rel="stylesheet" href="https://fonts.googleapis.com/css2?family=Open+Sans:wght@400;600;700&family=Russo+One&display=swap">
<style>
  :root {
    --page-bg: #e6e3de;
    --card-black: #0d0d0e;
    --silver: #c9cbcf;
    --accent: #f2542d;
    --accent-deep: #d8321b;
    --text-light: #f1f1f1;
    --text-muted: #cfcfcf;
  }
  * { margin: 0; padding: 0; box-sizing: border-box; }
  html, body {
    width: 1200px; height: 1023px; overflow: hidden;
    background: var(--page-bg);
  }
  .card {
    position: absolute; left: 100px; top: 226px;
    width: 1000px; height: 571px;
    border-radius: 6px; overflow: hidden;
    background: linear-gradient(160deg, #1a1a1c 0%, var(--card-black) 55%, #050505 100%);
    box-shadow: 0 18px 40px rgba(0,0,0,.35);
    font-family: "Open Sans", sans-serif;
  }
  .card-shape { position: absolute; inset: 0; }
  .logo-area {
    position: absolute; left: 60px; top: 200px; width: 360px;
    display: flex; align-items: center; gap: 16px;
  }
  .logo-mark {
    width: 50px; height: 50px; flex: none; border-radius: 50%;
    background: var(--accent);
  }
  .logo-name {
    font-weight: 700; font-size: 34px; line-height: 1.1; color: var(--silver);
  }
  .contact {
    position: absolute; right: 56px; top: 64px;
    text-align: right; color: var(--text-light);
  }
  .person-name {
    font-family: "Russo One", sans-serif; font-size: 38px;
    color: var(--accent); letter-spacing: 1px; text-transform: uppercase;
  }
  .person-role {
    font-weight: 700; font-size: 18px; letter-spacing: 1px;
    text-transform: uppercase; margin-bottom: 20px; color: var(--text-light);
  }
  .contact-row {
    display: flex; justify-content: flex-end; align-items: center;
    gap: 12px; font-size: 18px; line-height: 34px; color: var(--text-light);
  }
  .contact-icon {
    width: 22px; height: 22px; flex: none; border-radius: 4px;
    background: var(--accent-deep);
    display: flex; align-items: center; justify-content: center;
  }
  .contact-icon svg { width: 14px; height: 14px; }
  .hours-title {
    margin-top: 24px; font-weight: 600; font-size: 20px; color: var(--accent);
    padding-right: 34px;
  }
  .hours-line {
    font-size: 18px; line-height: 32px; color: var(--text-muted); padding-right: 34px;
  }
</style>
</head>
<body>
  <section class="card">
    <svg class="card-shape" viewBox="0 0 1000 571" width="1000" height="571" aria-hidden="true">
      <defs>
        <linearGradient id="panelFill" x1="0" y1="0" x2="1" y2="1">
          <stop offset="0" stop-color="#2a2a2d"/>
          <stop offset="1" stop-color="#141415"/>
        </linearGradient>
        <linearGradient id="silverLine" x1="0" y1="0" x2="0" y2="1">
          <stop offset="0" stop-color="#eeeeee"/>
          <stop offset="1" stop-color="#6f7277"/>
        </linearGradient>
      </defs>
      <path d="M0,0 H320 C380,0 390,110 430,140 C490,185 505,260 485,340 C465,430 420,470 465,571 H0 Z"
            fill="url(#panelFill)"/>
      <path d="M320,0 C380,0 390,110 430,140 C490,185 505,260 485,340 C465,430 420,470 465,571"
            fill="none" stroke="url(#silverLine)" stroke-width="5"/>
    </svg>

    <div class="logo-area">
      <span class="logo-mark"></span>
      <span class="logo-name">Wren Vehicle Polishing</span>
    </div>

    <div class="contact">
      <div class="person-name">Dana Reyes</div>
      <div class="person-role">Director</div>

      <div class="contact-row">
        <span>070 555 0142</span>
        <span class="contact-icon"><svg viewBox="0 0 16 16"><path d="M4 1 L6 5 L4.5 6.5 C5.5 8.5 7.5 10.5 9.5 11.5 L11 10 L15 12 L14 15 C7 15 1 9 1 2 Z" fill="#fff"/></svg></span>
      </div>
      <div class="contact-row">
        <span>070 555 0187</span>
        <span class="contact-icon"><svg viewBox="0 0 16 16"><rect x="4" y="1" width="8" height="14" rx="1.5" fill="#fff"/><rect x="5.5" y="3" width="5" height="8" fill="#d8321b"/></svg></span>
      </div>
      <div class="contact-row">
        <span>wrenpolishcrew@mailbox-demo.net</span>
        <span class="contact-icon"><svg viewBox="0 0 16 16"><rect x="1" y="3" width="14" height="10" fill="#fff"/><path d="M1 3 L8 9 L15 3" fill="none" stroke="#d8321b" stroke-width="1.5"/></svg></span>
      </div>
      <div class="contact-row">
        <span>www.socialpage-demo.net/wrenpolishKTR</span>
        <span class="contact-icon"><svg viewBox="0 0 16 16"><circle cx="8" cy="8" r="6.5" fill="none" stroke="#fff" stroke-width="1.5"/><ellipse cx="8" cy="8" rx="2.8" ry="6.5" fill="none" stroke="#fff" stroke-width="1.2"/><path d="M1.5 8 H14.5" stroke="#fff" stroke-width="1.2"/></svg></span>
      </div>

      <div class="hours-title">Hours of operation</div>
      <div class="hours-line">Mon - Fri 7:00AM to 8:00PM</div>
      <div class="hours-line">Sat - 10:00AM to 8:00PM</div>
    </div>
  </section>
</body>
</html>
```